Labour Day banner showcasing 20% off site

Banner graphic promoting our Labour Day sale
Size: 2000px x 600px
- examples from other companies and their sale banners have been uploaded for inspiration. Labour day examples are for the United States's holiday and submissions should NOT be in their country colours.
- product images can be found at www.tallpinegreens.com

Target Market(s)

19+

Industry/Entity Type

Cannabis

Requirements
Must have
• Phrases:
- “Happy Labour Day”
- “20% off site wide sale*"
- "Coupon code: Harvest20"
- Underneath phrase the date of sale “September 3rd - 7th”
- In tiny print “*excludes all sale and bundled items”
- MUST BE 2000px x 600px
Nice to have
• - images of the products or bud we carry which can be found at www.tallpinegreens.com
- bold
Should not have
• - company logo
- the American flag, we are a Canadian company, colours and flag should all be Canadian

```html
<!DOCTYPE html>
<html lang="en">
<head>
<meta charset="utf-8">
<title>Happy Labour Day – 20% off site wide sale</title>
<link rel="stylesheet" href="https://fonts.googleapis.com/css2?family=Permanent+Marker&family=Open+Sans:wght@400;700;800&display=swap">
<style>
  :root {
    --sky-top: #47cdf4;
    --sky-mid: #a6e6fb;
    --sky-low: #eef9fe;
    --title-blue: #2a3ce6;
    --ink: #111111;
    --white: #ffffff;
    --wood: #d8a64c;
    --wood-dark: #b7832c;
    --pin: #e0243a;
    --grass-top: #9be04a;
    --grass-mid: #4fb81f;
    --grass-low: #2e8d12;
    --cloud-white: #f7fbff;
    --cloud-blue: #8ec8ef;
  }
  * { margin: 0; padding: 0; box-sizing: border-box; }
  html, body { width: 1200px; height: 360px; overflow: hidden; background: var(--white); }
  .banner {
    position: relative;
    width: 1200px;
    height: 360px;
    overflow: hidden;
    font-family: "Open Sans", Arial, sans-serif;
    color: var(--ink);
    background: linear-gradient(180deg, var(--sky-top) 0%, var(--sky-mid) 45%, var(--sky-low) 85%);
  }
  .cloud {
    position: absolute;
    border-radius: 50%;
    filter: blur(3px);
  }
  .cloud--left {
    left: 14px; top: 32px; width: 236px; height: 112px;
    background: radial-gradient(ellipse at 45% 45%, var(--cloud-white) 0%, #e4f2fb 50%, rgba(200,230,250,0) 72%);
  }
  .cloud--right {
    left: 876px; top: 38px; width: 314px; height: 176px;
    border-radius: 46% 54% 50% 50%;
    background: radial-gradient(ellipse at 55% 50%, var(--cloud-white) 0%, #eef7fe 48%, var(--cloud-blue) 66%, rgba(142,200,239,0) 74%);
  }
  .title {
    position: absolute;
    left: 285px; top: 16px; width: 570px;
    text-align: center;
    font-family: "Permanent Marker", "Comic Sans MS", cursive;
    font-weight: 400;
    font-size: 58px;
    line-height: 1;
    color: var(--title-blue);
    letter-spacing: 1px;
    text-transform: uppercase;
    text-shadow: 3px 3px 0 var(--white), -1px -1px 0 var(--white), 1px -1px 0 var(--white), -1px 1px 0 var(--white);
    white-space: nowrap;
  }
  .title .cap { font-size: 82px; }
  .subtitle {
    position: absolute;
    left: 370px; top: 122px; width: 410px;
    text-align: center;
    font-size: 38px;
    font-weight: 400;
    letter-spacing: -0.5px;
    white-space: nowrap;
  }
  .subtitle sup { font-size: 18px; vertical-align: 18px; margin-left: 2px; }
  .coupon {
    position: absolute;
    left: 990px; top: 100px;
    transform: rotate(12deg);
    transform-origin: left top;
    font-weight: 800;
    white-space: nowrap;
  }
  .coupon__label { display: block; font-size: 15px; margin-left: 22px; }
  .coupon__code { display: block; font-size: 31px; line-height: 1.05; letter-spacing: -0.5px; }
  .coupon__star { position: absolute; left: 965px; top: 112px; font-size: 14px; font-weight: 700; }
  .dates {
    position: absolute;
    left: 893px; top: 252px;
    font-size: 31px;
    font-weight: 800;
    letter-spacing: -1px;
    white-space: nowrap;
  }
  .board {
    position: absolute;
    top: 208px;
    height: 108px;
    border: 5px solid var(--wood);
    outline: 1px solid var(--wood-dark);
    background: var(--white);
    padding: 6px;
  }
  .board::before, .board::after {
    content: "";
    position: absolute;
    top: -3px;
    width: 6px; height: 6px;
    border-radius: 50%;
    background: var(--pin);
  }
  .board::before { left: 2px; }
  .board::after { right: 2px; }
  .board__photo { width: 100%; height: 100%; }
  .board--1 { left: 60px; width: 97px; }
  .board--2 { left: 185px; width: 98px; }
  .board--3 { left: 307px; width: 97px; }
  .board--4 { left: 429px; width: 99px; }
  .board--5 { left: 558px; width: 99px; }
  .photo--cartridges { background: linear-gradient(90deg, #fff 20%, #1a1a14 30%, #c9a31c 40%, #111 50%, #c9a31c 60%, #1a1a14 70%, #fff 80%); }
  .photo--wax { background: linear-gradient(135deg, #c0392b 0%, #f4efe0 45%, #efe6cf 100%); }
  .photo--tincture { background: linear-gradient(90deg, #fff 15%, #2b2b2b 30%, #2b2b2b 42%, #d9c9a8 50%, #5fb8a0 70%, #fff 85%); }
  .photo--bud { background: radial-gradient(ellipse at 50% 50%, #6e7a4a 0%, #4d5a36 45%, #fff 70%); }
  .photo--shatter { background: linear-gradient(135deg, #e8d230 0%, #d4b81e 35%, #1b1a12 60%, #c8a818 100%); }
  .grass {
    position: absolute;
    left: 0; top: 300px; width: 1200px; height: 60px;
    background: linear-gradient(180deg, rgba(155,224,74,0) 0%, var(--grass-top) 12%, var(--grass-mid) 55%, var(--grass-low) 100%);
  }
  .footnote {
    position: absolute;
    left: 14px; top: 329px;
    font-size: 19px;
    font-weight: 700;
    color: var(--white);
    text-shadow: 1px 1px 2px rgba(0,0,0,0.45);
    white-space: nowrap;
  }
  .footnote__star { font-size: 12px; margin-right: 8px; vertical-align: 2px; }
</style>
</head>
<body>
<main class="banner">
  <div class="cloud cloud--left" role="img" aria-label="Soft white cloud in the sky"></div>
  <div class="cloud cloud--right" role="img" aria-label="Large white cloud holding the coupon code"></div>

  <h1 class="title"><span class="cap">H</span>appy <span class="cap">L</span>abour <span class="cap">D</span>ay</h1>
  <p class="subtitle">20% off site wide sale<sup>✷</sup></p>

  <span class="coupon__star">✷</span>
  <p class="coupon">
    <span class="coupon__label">Coupon code</span>
    <span class="coupon__code">Harvest20</span>
  </p>

  <p class="dates">september 3 - 7th</p>

  <div class="board board--1"><div class="board__photo photo--cartridges" role="img" aria-label="Product photo: vape cartridges and tube"></div></div>
  <div class="board board--2"><div class="board__photo photo--wax" role="img" aria-label="Product photo: white wax bar and package"></div></div>
  <div class="board board--3"><div class="board__photo photo--tincture" role="img" aria-label="Product photo: CBD tincture bottle and box"></div></div>
  <div class="board board--4"><div class="board__photo photo--bud" role="img" aria-label="Product photo: cannabis bud"></div></div>
  <div class="board board--5"><div class="board__photo photo--shatter" role="img" aria-label="Product photo: shatter concentrate and pouch"></div></div>

  <div class="grass" role="img" aria-label="Green grass along the bottom"></div>

  <p class="footnote"><span class="footnote__star">✷</span>excludes all sale and bundled items</p>
</main>
</body>
</html>
```